Medical Waste Company with Logo

Need a business card design that targets office managers in the medical community. This card will be the front line for our sales team to market our services to the community. We would like to have email, phone number, website. Please use the logo attached to create a design that we would be proud of.

Target Market(s)

Medical Clients

Industry/Entity Type

Medical Supply

Contact Information for Business Card

Please use logo attached

Colors

Designer to choose colors to be used in the design.

Requirements
Must have
• Our logo (see attached file)
Nice to have
• Maybe a pop of some sort, raised..?

```html
<!DOCTYPE html>
<html lang="en">
<head>
<meta charset="utf-8">
<title>Northpeak Clinical Disposal – Business Card</title>
<link href="https://fonts.googleapis.com/css2?family=Montserrat:wght@500;600&family=Lato:wght@400&display=swap" rel="stylesheet">
<style>
  :root {
    --backdrop: #8c8c8c;
    --card-white: #f3f3f3;
    --brand-blue: #0d6399;
    --brand-grey: #878787;
    --ink: #222222;
    --white: #ffffff;
  }
  * { box-sizing: border-box; margin: 0; padding: 0; }
  html, body { width: 1200px; height: 1200px; overflow: hidden; }
  body { background: var(--backdrop); position: relative; font-family: "Lato", sans-serif; }

  .card { position: absolute; top: 310px; height: 594px; border-radius: 16px; overflow: hidden; box-shadow: 3px 4px 6px rgba(0,0,0,0.35); }
  .card-front { left: 234px; width: 363px; background: var(--card-white); }
  .card-back { left: 627px; width: 370px; background: var(--brand-grey); }

  .brand-mark-front {
    position: absolute; left: 50%; top: 118px; width: 84px; height: 84px;
    margin-left: -42px; border-radius: 50%; background: var(--brand-blue);
  }
  .brand-name {
    position: absolute; left: 0; right: 0; top: 212px; text-align: center;
    font-family: "Montserrat", sans-serif; font-weight: 600; font-size: 25px;
    color: var(--brand-blue); letter-spacing: 0.5px;
  }
  .brand-tagline {
    position: absolute; left: 27px; right: 27px; top: 248px;
    display: flex; align-items: center; gap: 10px;
    font-family: "Montserrat", sans-serif; font-weight: 600; font-size: 19px;
    color: var(--brand-blue); letter-spacing: 9px;
  }
  .brand-tagline::before, .brand-tagline::after {
    content: ""; flex: 1; height: 2px; background: var(--brand-blue);
  }

  .person-name {
    position: absolute; left: 0; right: 0; top: 404px; text-align: center;
    font-family: "Montserrat", sans-serif; font-weight: 600; font-size: 21px; color: var(--brand-blue);
  }
  .person-role {
    position: absolute; left: 0; right: 0; top: 428px; text-align: center;
    font-size: 16px; color: var(--ink);
  }
  .contact-icons { position: absolute; left: 90px; top: 468px; }
  .contact-list {
    position: absolute; left: 0; right: 0; top: 495px; text-align: center;
    list-style: none; font-size: 16px; line-height: 22px; color: var(--ink);
  }

  .back-blue { position: absolute; left: 0; top: 0; width: 100%; height: 410px; background: var(--brand-blue); }
  .brand-mark-back {
    position: absolute; left: 50%; top: 170px; width: 110px; height: 110px;
    margin-left: -55px; border-radius: 50%; background: var(--white);
  }
  .back-brand {
    position: absolute; left: 0; right: 0; top: 310px; text-align: center;
    font-family: "Montserrat", sans-serif; font-weight: 600; font-size: 28px;
    line-height: 36px; color: var(--white); letter-spacing: 1px;
  }
  .back-website {
    position: absolute; left: 0; right: 0; top: 532px; text-align: center;
    font-family: "Montserrat", sans-serif; font-weight: 500; font-size: 15px;
    color: var(--white); letter-spacing: 3.5px;
  }
</style>
</head>
<body>
  <section class="card card-front">
    <div class="brand-mark-front" aria-hidden="true"></div>
    <div class="brand-name">NORTHPEAK CLINICAL</div>
    <div class="brand-tagline">DISPOSAL</div>

    <div class="person-name">DANIEL HARPER</div>
    <div class="person-role">Managing Director</div>

    <svg class="contact-icons" width="188" height="22" viewBox="0 0 188 22" aria-hidden="true">
      <line x1="0" y1="11" x2="58" y2="11" stroke="#888" stroke-width="1"/>
      <line x1="130" y1="11" x2="188" y2="11" stroke="#888" stroke-width="1"/>
      <circle cx="69" cy="11" r="10" fill="#0d6399"/>
      <path d="M64.5 6.5 l2.5 -0.5 1.2 3 -1.5 1 a7 7 0 0 0 3.3 3.3 l1 -1.5 3 1.2 -0.5 2.5 a9 9 0 0 1 -9 -9z" fill="#fff"/>
      <circle cx="92" cy="11" r="10" fill="#0d6399"/>
      <rect x="86.5" y="7" width="11" height="8" fill="#fff"/>
      <path d="M86.5 7 l5.5 4.5 5.5 -4.5" fill="none" stroke="#0d6399" stroke-width="1"/>
      <circle cx="115" cy="11" r="10" fill="#0d6399"/>
      <circle cx="115" cy="11" r="5.5" fill="none" stroke="#fff" stroke-width="1.4"/>
      <line x1="109.5" y1="11" x2="120.5" y2="11" stroke="#fff" stroke-width="1.2"/>
      <ellipse cx="115" cy="11" rx="2.3" ry="5.5" fill="none" stroke="#fff" stroke-width="1.2"/>
    </svg>

    <ul class="contact-list">
      <li>555 201 7734</li>
      <li>hello@northpeakclinical.com</li>
      <li>www.northpeakclinical.com</li>
    </ul>
  </section>

  <section class="card card-back">
    <div class="back-blue"></div>
    <div class="brand-mark-back" aria-hidden="true"></div>
    <div class="back-brand">NORTHPEAK<br>CLINICAL DISPOSAL</div>
    <div class="back-website">www.northpeakclinical.com</div>
  </section>
</body>
</html>
```